Email signatures and letterhead for in-house lawyers and staff

I need Word, Outlook, and Gmail compatible letterhead and email signature block for an in-house litigation group. Simple and generic is the goal! The design must be user-modifiable for several locations and job titles. The design will work best if created in MS Word. We are an in-house group of trial lawyers, about 40 persons total, operating from nine locations, and providing services in ten US states. Letterhead will be used in header of MSWord documents. Email sig will be used in both Outlook and Gmail. The office name will be different in each of our locations, so the design has to be user-modifiable.

Industry/Entity Type

Law Firm

Font styles to use
Sans Serif

Requirements
Must have
• A fresher, more professional look than the screenshots I've posted

The screenshot with multiple attorney names in the office is most representative of the info we want included.
Nice to have
• Sylish but not overly so. Generic legal symbols might be appropriate, but can't look like tired old clip art.
Should not have
• watermarks

```html
<!DOCTYPE html>
<html lang="en">
<head>
<meta charset="utf-8">
<title>Harlow Trial Group – Letterhead</title>
<link rel="stylesheet" href="https://fonts.googleapis.com/css2?family=Lato:wght@400;700&family=Roboto+Condensed:wght@300;400&display=swap">
<style>
  :root {
    --backdrop: #d6d6d6;
    --paper: #ffffff;
    --ink: #111111;
    --heading: #4a4a4a;
    --body-text: #5a5a5a;
    --rule: #2a2a2a;
    --band-grey: #9a9a9a;
  }
  html, body {
    margin: 0;
    padding: 0;
    width: 1056px;
    height: 1200px;
    overflow: hidden;
    background: var(--backdrop);
  }
  .letterhead {
    position: absolute;
    left: 104px;
    top: 0;
    width: 848px;
    height: 1200px;
    background: var(--paper);
    font-family: "Lato", sans-serif;
    color: var(--heading);
  }
  .firm-mark {
    position: absolute;
    left: 91px;
    top: 116px;
    display: flex;
    align-items: center;
    gap: 10px;
    font-family: "Lato", sans-serif;
    font-weight: 700;
    font-size: 20px;
    line-height: 1.2;
    color: var(--ink);
    width: 150px;
  }
  .firm-mark .mark-square {
    flex: none;
    width: 14px;
    height: 14px;
    background: var(--ink);
  }
  .office-block {
    position: absolute;
    right: calc(848px - 540px);
    top: 78px;
    text-align: right;
  }
  .office-name {
    font-size: 14px;
    line-height: 20px;
    margin: 0 0 2px;
  }
  .attorney-list {
    margin: 0;
    padding: 0;
    list-style: none;
    font-weight: 700;
    font-size: 20px;
    line-height: 24px;
  }
  .header-divider {
    position: absolute;
    left: 565px;
    top: 75px;
    width: 1.5px;
    height: 101px;
    background: var(--rule);
  }
  .contact-block {
    position: absolute;
    left: 584px;
    top: 72px;
    font-size: 14px;
    line-height: 19px;
  }
  .address {
    margin: 0 0 6px;
    font-style: normal;
  }
  .contact-line {
    display: flex;
    align-items: center;
    height: 22px;
  }
  .contact-line svg {
    width: 14px;
    height: 14px;
    margin-right: 16px;
    fill: var(--ink);
  }
  .letter-body {
    position: absolute;
    left: 78px;
    width: 688px;
    font-family: "Roboto Condensed", sans-serif;
    font-weight: 300;
    font-size: 18px;
    line-height: 29.5px;
    color: var(--body-text);
    text-align: justify;
  }
  .letter-body p { margin: 0; position: absolute; left: 0; width: 688px; }
  .salutation { top: 0; }
  .para-1 { top: 56px; }
  .para-2 { top: 203px; }
  .para-3 { top: 321px; }
  .para-4 { top: 440px; }
  .closing { top: 591px; }
  .signature {
    position: absolute;
    left: 78px;
    top: 1024px;
    width: 82px;
    height: 44px;
    background: linear-gradient(180deg, #f2f2f2, #e6e6e6);
  }
  .footer-bands {
    position: absolute;
    left: 0;
    bottom: 0;
    width: 848px;
    height: 31px;
    display: block;
  }
</style>
</head>
<body>
  <main class="letterhead">
    <header>
      <div class="firm-mark"><span class="mark-square"></span><span>Harlow Trial Group</span></div>

      <div class="office-block">
        <p class="office-name">Office Name</p>
        <ul class="attorney-list">
          <li>Daniel Harlow,</li>
          <li>Renata Quill,</li>
          <li>Owen Pritchard.</li>
        </ul>
      </div>

      <div class="header-divider"></div>

      <div class="contact-block">
        <address class="address">4810 Ridgeline Pkwy, Suite 312<br>Fairmont, ZQ 40217</address>
        <div class="contact-line">
          <svg viewBox="0 0 24 24" aria-hidden="true"><path d="M6.6 10.8a15.2 15.2 0 0 0 6.6 6.6l2.2-2.2a1 1 0 0 1 1-.25 11.4 11.4 0 0 0 3.6.57 1 1 0 0 1 1 1V20a1 1 0 0 1-1 1A17 17 0 0 1 3 4a1 1 0 0 1 1-1h3.5a1 1 0 0 1 1 1c0 1.25.2 2.45.57 3.57a1 1 0 0 1-.25 1z"/></svg>
          <span>(555) 204-3180</span>
        </div>
        <div class="contact-line">
          <svg viewBox="0 0 24 24" aria-hidden="true"><path d="M6 2h12v5H6zM4 8h16a2 2 0 0 1 2 2v7h-4v5H6v-5H2v-7a2 2 0 0 1 2-2zm4 8v4h8v-4z"/></svg>
          <span>(555) 204-3191</span>
        </div>
        <div class="contact-line">
          <svg viewBox="0 0 24 24" aria-hidden="true"><path d="M2 5h20v14H2zm2 2v.5l8 5.5 8-5.5V7l-8 5.5z"/></svg>
          <span>d.harlow@harlowtrial.example</span>
        </div>
      </div>
    </header>

    <section class="letter-body" style="top:397px;">
      <p class="salutation">Dear Sir/Mam,</p>
      <p class="para-1">Contrary to popular belief, Lorem Ipsum is not simply random text. It has roots in a piece of classical Latin literature from 45 BC, making it over 2000 years old. Edwin Marlowe, a Latin professor at Larkfield College in Virginia, looked up one of the more obscure Latin words, consectetur.</p>
      <p class="para-2">Lorem Ipsum comes from sections 1.10.32 and 1.10.33 of "de Finibus Bonorum et Malorum" (The Extremes of Good and Evil) by Aurelian Vesto, written in 45 BC. This book is a treatise on the theory of ethics, very popular during the Renaissance. The first line of Lorem Ipsum.</p>
      <p class="para-3">The standard chunk of Lorem Ipsum used since the 1500s is reproduced below for those interested. Sections 1.10.32 and 1.10.33 from "de Finibus Bonorum et Malorum" by Aurelian Vesto are also reproduced in their exact original.</p>
      <p class="para-4">The standard chunk of Lorem Ipsum used since the 1500s is reproduced below for those interested.</p>
      <p class="closing">Best Regards</p>
    </section>

    <div class="signature" role="img" aria-label="Handwritten signature of the sender"></div>

    <svg class="footer-bands" viewBox="0 0 848 31" preserveAspectRatio="none" aria-hidden="true">
      <polygon points="0,6 209,6 204,12 0,12" fill="var(--band-grey)"/>
      <polygon points="211,6 431,6 426,12 206,12" fill="var(--ink)"/>
      <polygon points="433,6 649,6 644,12 428,12" fill="var(--band-grey)"/>
      <polygon points="666,0 848,0 848,31 0,31 0,20 644,20" fill="var(--ink)"/>
    </svg>
  </main>
</body>
</html>
```